Meurtre chez la Vern‘

“Vern’” is the informal nickname used inside the French police for the "Escouade Vernaleuse du Nord", an elite homicide unit. The apostrophe reflects spoken language and internal slang. The title Meurtre chez la Vern’ highlights the central irony of the novel: a murder committed inside the very place meant to investigate murders.
Summary
A woman’s body is found inside the offices of Paris’s elite homicide squad. As detectives investigate, they uncover buried cases, internal rivalries and institutional silence. The closer they get to the truth, the clearer it becomes: this crime was meant to stay hidden.
Keywords : Woman’s body, Police procedural, Murder inside the police, Elite homicide unit, Dark realism, 58 rue Bastelinou.
Size : 16 x 24 cm
Title : Meurtre chez la Vern'
Author : Lucien Maréchaux
Publisher : Editions Torvelle (at the bottom of the page)
Book

```html
<!DOCTYPE html>
<html lang="fr">
<head>
<meta charset="utf-8">
<title>Meurtre chez la Vern’ — Lucien Maréchaux</title>
<link rel="stylesheet" href="https://fonts.googleapis.com/css2?family=Big+Shoulders+Display:wght@800&family=Barlow+Condensed:wght@400&display=swap">
<style>
  :root {
    --red-deep: #6c0405;
    --red-mid: #7d0a0b;
    --red-light: #8a1012;
    --cream: #f7efd8;
  }
  html, body {
    margin: 0;
    padding: 0;
    width: 800px;
    height: 1200px;
    overflow: hidden;
    background: var(--red-deep);
  }
  .cover {
    position: relative;
    width: 800px;
    height: 1200px;
    overflow: hidden;
  }
  .cover-photo {
    position: absolute;
    inset: 0;
    background: linear-gradient(180deg, var(--red-deep) 0%, var(--red-mid) 55%, var(--red-light) 80%, var(--red-light) 100%);
  }
  .author {
    position: absolute;
    left: 115px;
    top: 226px;
    margin: 0;
    font-family: "Barlow Condensed", sans-serif;
    font-weight: 400;
    font-size: 46px;
    line-height: 1;
    letter-spacing: -0.5px;
    color: var(--cream);
    text-transform: uppercase;
  }
  .title {
    position: absolute;
    left: 114px;
    top: 268px;
    margin: 0;
    font-family: "Big Shoulders Display", sans-serif;
    font-weight: 800;
    color: var(--cream);
    text-transform: uppercase;
  }
  .title span { display: block; line-height: 1; }
  .title .line-main {
    font-size: 196px;
    height: 182px;
    letter-spacing: 2px;
  }
  .title .line-small {
    font-size: 118px;
    height: 132px;
    letter-spacing: 2px;
  }
  .imprint-mark {
    position: absolute;
    left: 119px;
    top: 789px;
    width: 120px;
    height: 120px;
  }
  .publisher {
    position: absolute;
    left: 0;
    right: 0;
    top: 1110px;
    margin: 0;
    text-align: center;
    font-family: "Barlow Condensed", sans-serif;
    font-weight: 400;
    font-size: 31px;
    line-height: 1;
    color: var(--cream);
    text-transform: uppercase;
  }
</style>
</head>
<body>
  <main class="cover">
    <div class="cover-photo" role="img" aria-label="Photographie monochrome rouge de la façade d’un immeuble de police avec fenêtres, drapeaux, grille et panneau d’entrée"></div>

    <p class="author">Lucien Maréchaux</p>

    <h1 class="title">
      <span class="line-main">Meurtre</span>
      <span class="line-small">chez la</span>
      <span class="line-main">Vern’</span>
    </h1>

    <svg class="imprint-mark" viewBox="0 0 120 120" aria-label="Torvelle">
      <circle cx="60" cy="60" r="58" fill="none" stroke="#f7efd8" stroke-width="2"/>
      <text x="60" y="67" text-anchor="middle" font-family="Barlow Condensed, sans-serif" font-size="20" fill="#f7efd8">TORVELLE</text>
    </svg>

    <p class="publisher">Editions Torvelle</p>
  </main>
</body>
</html>
```